Business card and Logo for a private personal training studio

We need a business card and logo for a private personal training studio.

The studios name is "Harbour Stone Rise"
Main coloring to be a bright light blue. Looking for a crisp modern look

The front of the card is to have the

Studios name.
The Logo
Private Personal Training Studio
Kim Larden
0452 614 298

The back of the card is to have a lot of words relating to the services we offer. Please place the words vertically and horizontally using different fonts, different text sizes, different boldness and different colors to create a word picture.

Main words that need highlighting are

QVK, PILATES, BOXING, SPIN, STRENGTH, WEIGHT LOSS, BALANCE

Other words to add to the mix with less emphasis

Fitness, Conditioning, Lifestyle, Wellness, Health, Energy, Cardio, Goals, Muscle Tone, Vitality, Confidence, Attitude, Determination, Motivation, Dedication, Fun

Target Market(s)

Woman aged 30 to 60

Industry/Entity Type

Personal Trainer

Contact Information for Business Card

Harbour Stone Rise
Kim Larden
0452 614 298

Colors
0493ce
33a6d7
85cae6

```html
<!DOCTYPE html>
<html lang="en">
<head>
<meta charset="utf-8">
<title>Harbour Stone Rise – Business Card</title>
<link rel="stylesheet" href="https://fonts.googleapis.com/css2?family=Aleo:wght@300;400;700&family=Arimo:wght@400;700&family=Oswald:wght@600&family=Roboto+Condensed:wght@700&display=swap">
<style>
  :root {
    --bg: #bcbdbf;
    --card-dark: #000000;
    --card-light: #ffffff;
    --blue-deep: #0493ce;
    --blue-mid: #33a6d7;
    --blue-light: #85cae6;
    --grey: #a3a4a6;
    --grey-mark: #a9a9aa;
    --white: #ffffff;
    --ink: #111111;
  }
  html, body {
    margin: 0;
    width: 1200px;
    height: 934px;
    overflow: hidden;
    background: var(--bg);
  }
  .stage {
    position: relative;
    width: 1151px;
    height: 896px;
    transform: scale(1.0426, 1.0424);
    transform-origin: 0 0;
  }
  .card {
    position: absolute;
    top: 100px;
    height: 696px;
    border-radius: 28px;
    box-shadow: 4px 8px 18px rgba(0,0,0,0.28);
    overflow: hidden;
  }
  .card--back { left: 100px; width: 426px; background: var(--card-dark); }
  .card--front { left: 626px; width: 424px; background: var(--card-light); }

  /* services word picture (coordinates relative to the back card) */
  .word-cloud { position: absolute; left: 0; top: 40px; width: 426px; height: 620px; }
  .word {
    position: absolute;
    margin: 0;
    line-height: 1;
    white-space: nowrap;
  }
  .down { writing-mode: vertical-rl; }
  .up { writing-mode: vertical-rl; transform: rotate(180deg); }

  .serif-light { font-family: "Aleo", Georgia, serif; font-weight: 300; }
  .serif { font-family: "Aleo", Georgia, serif; font-weight: 400; }
  .serif-bold { font-family: "Aleo", Georgia, serif; font-weight: 700; }
  .sans { font-family: "Arimo", Arial, sans-serif; font-weight: 400; }
  .sans-bold { font-family: "Arimo", Arial, sans-serif; font-weight: 700; }
  .condensed { font-family: "Roboto Condensed", "Arial Narrow", sans-serif; font-weight: 700; }

  .w-strength { left: 60px; top: 120px; font-size: 38px; color: var(--blue-deep); }
  .w-pilates { left: 330px; top: 120px; font-size: 32px; color: var(--grey); }
  .w-wellness { left: 374px; top: 122px; font-size: 22px; color: var(--white); }
  .w-fitness { left: 60px; top: 168px; font-size: 24px; color: var(--white); }
  .w-vitality { left: 162px; top: 168px; font-size: 24px; color: var(--blue-light); }
  .w-boxing { left: 60px; top: 204px; font-size: 36px; color: var(--white); }
  .w-fun { left: 226px; top: 208px; font-size: 30px; color: var(--blue-mid); }
  .w-weightloss { left: 60px; top: 250px; font-size: 33px; color: var(--grey); }
  .w-balance { left: 60px; top: 298px; font-size: 32px; color: var(--blue-light); }
  .w-determination { left: 104px; top: 298px; font-size: 19px; color: var(--grey); }
  .w-muscletone { left: 140px; top: 298px; font-size: 28px; color: var(--blue-mid); }
  .w-spin { left: 318px; top: 300px; font-size: 42px; color: var(--blue-mid); }
  .w-cardio { left: 376px; top: 300px; font-size: 21px; color: var(--white); }
  .w-motivation { left: 140px; top: 336px; font-size: 25px; color: var(--blue-light); }
  .w-confidence { left: 140px; top: 372px; font-size: 19px; color: var(--white); }
  .w-lifestyle { left: 378px; top: 380px; font-size: 19px; color: var(--blue-mid); }
  .w-conditioning { left: 140px; top: 400px; font-size: 21px; color: var(--blue-mid); }
  .w-qvk { left: 140px; top: 432px; font-size: 42px; color: var(--blue-light); }
  .w-goals { left: 246px; top: 442px; font-size: 27px; color: var(--white); }
  .w-energy { left: 60px; top: 490px; font-size: 32px; color: var(--blue-deep); }
  .w-health { left: 184px; top: 496px; font-size: 24px; color: var(--blue-light); }
  .w-attitude { left: 282px; top: 494px; font-size: 23px; color: var(--grey); }
  .w-dedication { left: 60px; top: 536px; font-size: 23px; color: var(--white); }

  /* front */
  .brand {
    position: absolute;
    left: 0; right: 0; top: 52px;
    text-align: center;
  }
  .brand__square {
    display: block;
    width: 150px; height: 150px;
    margin: 26px auto 0;
    background: var(--blue-deep);
  }
  .brand__name {
    margin: 44px 0 0;
    font-family: "Oswald", "Arial Narrow", sans-serif;
    font-weight: 600;
    font-size: 40px;
    line-height: 1;
    letter-spacing: 0.5px;
    color: var(--grey-mark);
    white-space: nowrap;
  }
  .brand__tagline {
    margin: 6px 0 0;
    font-family: "Aleo", Georgia, serif;
    font-weight: 400;
    font-size: 19px;
    color: var(--grey);
    letter-spacing: 0.4px;
  }
  .contact {
    position: absolute;
    left: 0; right: 0; top: 478px;
    text-align: center;
    font-family: "Arimo", Arial, sans-serif;
    color: var(--ink);
  }
  .contact__name {
    margin: 0 0 20px;
    font-weight: 700;
    font-size: 29px;
    letter-spacing: 0.5px;
  }
  .contact__line {
    margin: 0 0 8px;
    font-size: 20px;
    display: flex;
    justify-content: center;
    align-items: center;
    gap: 6px;
  }
  .contact__icon { width: 20px; height: 20px; fill: var(--blue-deep); }
</style>
</head>
<body>
<main class="stage">
  <section class="card card--back" aria-label="Card back: services word picture">
    <div class="word-cloud">
      <p class="word sans-bold w-strength">STRENGTH</p>
      <p class="word down sans-bold w-pilates">PILATES</p>
      <p class="word up serif w-wellness">Wellness</p>
      <p class="word sans-bold w-fitness">Fitness</p>
      <p class="word serif-bold w-vitality">Vitality</p>
      <p class="word sans w-boxing">BOXING</p>
      <p class="word serif w-fun">Fun</p>
      <p class="word serif-light w-weightloss">WEIGHT LOSS</p>
      <p class="word down sans-bold w-balance">BALANCE</p>
      <p class="word up sans-bold w-determination">Determination</p>
      <p class="word condensed w-muscletone">Muscle Tone</p>
      <p class="word down sans w-spin">SPIN</p>
      <p class="word down condensed w-cardio">Cardio</p>
      <p class="word serif w-motivation">Motivation</p>
      <p class="word sans-bold w-confidence">Confidence</p>
      <p class="word down sans w-lifestyle">Lifestyle</p>
      <p class="word sans-bold w-conditioning">Conditioning</p>
      <p class="word sans w-qvk">QVK</p>
      <p class="word sans w-goals">Goals</p>
      <p class="word serif-bold w-energy">Energy</p>
      <p class="word sans-bold w-health">Health</p>
      <p class="word serif w-attitude">Attitude</p>
      <p class="word serif w-dedication">Dedication</p>
    </div>
  </section>

  <section class="card card--front" aria-label="Card front">
    <div class="brand">
      <span class="brand__square" aria-hidden="true"></span>
      <h1 class="brand__name">HARBOUR STONE RISE</h1>
      <p class="brand__tagline">Private Personal Training Studio</p>
    </div>
    <div class="contact">
      <p class="contact__name">KIM LARDEN</p>
      <p class="contact__line">
        <svg class="contact__icon" viewBox="0 0 24 24" aria-hidden="true"><path d="M6.6 10.8a15.1 15.1 0 0 0 6.6 6.6l2.2-2.2a1 1 0 0 1 1-.25 11.4 11.4 0 0 0 3.6.57 1 1 0 0 1 1 1V20a1 1 0 0 1-1 1A17 17 0 0 1 3 4a1 1 0 0 1 1-1h3.5a1 1 0 0 1 1 1c0 1.25.2 2.450.57 3.57a1 1 0 0 1-.25 1z"/></svg>
        <span>0452 614 298</span>
      </p>
      <p class="contact__line">
        <svg class="contact__icon" viewBox="0 0 24 24" aria-hidden="true"><path d="M2 5h20v14H2z"/><path d="M3 6l9 7 9-7" fill="none" stroke="#fff" stroke-width="1.6"/></svg>
        <span>Kim@HarbourStoneRise.com</span>
      </p>
    </div>
  </section>
</main>
</body>
</html>
```